Bikes for Dreams - Website Redesign

Create a professional website for a nonprofit; BikesforDreams.org
Please see boatsforheroes.org and www.pedalsforhopes.org for the concept I am after.
The webpage should have a fun feel and should match the style of the company at www.pedalsforhopes.org. The pages to include are 'Home', 'About us' and 'Get Started'
Thank you and good luck!
Reason: i would like to see more designs.

```html
<!DOCTYPE html>
<html lang="en">
<head>
<meta charset="utf-8">
<title>Bikes for Dreams</title>
<link href="https://fonts.googleapis.com/css2?family=Lato:wght@400;700;900&display=swap" rel="stylesheet">
<style>
:root{
  --header:#2a9fd6;
  --hero-sky:#9fd9f2;
  --hero-deep:#3f9fd4;
  --navy:#0e5a7b;
  --form-blue:#1f8fcb;
  --red:#f4294f;
  --grey:#e8e8e8;
  --row:#d6d6d6;
  --section-blue:#3aa0d9;
  --btn-blue:#2d9ad8;
  --footer:#2f9bd7;
  --footer-dark:#1b6ea4;
  --ink:#222;
  --white:#fff;
}
*{box-sizing:border-box;margin:0;padding:0}
html,body{width:1200px;height:3169px;overflow:hidden}
body{position:relative;font-family:'Lato',sans-serif;color:var(--ink);background:var(--white)}
.abs{position:absolute}
.center{text-align:center}

/* header */
.site-header{left:0;top:0;width:1200px;height:190px;background:var(--header)}
.brand{left:118px;top:26px;display:flex;align-items:center;gap:14px;color:var(--white);font-weight:900;font-size:24px}
.brand-dot{width:40px;height:40px;border-radius:50%;background:var(--white)}
.phone{left:690px;top:48px;color:var(--white);font-weight:700;font-size:19px}
.btn-red{background:var(--red);color:var(--white);font-weight:700;border-radius:8px;text-align:center}
.header-donate{left:868px;top:36px;width:212px;height:44px;line-height:44px;font-size:20px}
.main-nav{left:535px;top:108px;display:flex}
.main-nav a{color:var(--white);text-decoration:none;font-weight:700;font-size:19px;margin-right:44px;padding-bottom:8px}
.main-nav a.active{border-bottom:3px solid var(--white)}

/* hero */
.hero{left:0;top:190px;width:1200px;height:660px;background:linear-gradient(180deg,var(--hero-sky) 0%,#8ccdef 60%,var(--hero-deep) 100%)}
.hero-art{left:100px;top:430px;width:740px;height:360px;background:linear-gradient(180deg,#57a9dc,#2e86c8);border-radius:6px;opacity:.55}
.hero-title{left:200px;top:280px;width:550px;font-size:27px;letter-spacing:3px;line-height:36px;color:var(--ink)}
.hero-donate{left:374px;top:363px;width:210px;height:42px;line-height:42px;font-size:20px}
.slide-arrow{top:418px}
.dots{left:548px;top:815px;display:flex;gap:14px}
.dots span{width:18px;height:18px;border-radius:50%;background:var(--white)}

.donate-form{left:849px;top:194px;width:309px;height:651px;background:var(--form-blue)}
.form-head{height:60px;background:var(--navy);color:var(--white);font-weight:700;font-size:19px;text-align:center;line-height:60px;letter-spacing:1px}
.form-field{position:absolute;left:16px;width:277px;height:36px;background:var(--white);border-radius:4px;font-size:15px;line-height:36px;padding-left:14px;color:#333}

/* donate car */
.intro-title{left:0;top:893px;width:1200px;font-size:34px;font-weight:700;letter-spacing:2px}
.intro-sub{left:0;top:940px;width:1200px;font-size:19px;letter-spacing:1.5px}
.btn-navy{background:var(--navy);color:var(--white);font-weight:700;font-size:18px;border-radius:6px;text-align:center}
.intro-btn{left:511px;top:983px;width:207px;height:42px;line-height:42px}

/* features */
.features{left:0;top:1061px;width:1200px;height:287px;background:var(--grey)}
.feature{width:260px;text-align:center}
.feature-circle{width:144px;height:144px;border-radius:50%;background:var(--navy);margin:0 auto;display:flex;align-items:center;justify-content:center}
.feature-label{margin-top:16px;font-size:17px;letter-spacing:1px;line-height:24px;color:#333}

/* how to donate */
.how{left:0;top:1348px;width:1200px;height:539px;background:var(--section-blue)}
.how-title{left:0;top:1408px;width:1200px;color:var(--white);font-size:34px;font-weight:700;letter-spacing:2px}
.kid{border-radius:40px;background:linear-gradient(180deg,#e24a6a,#2f57a8)}
.how-panel{left:161px;top:1479px;width:862px;height:342px;background:var(--white)}
.step{width:176px;text-align:center}
.step-tile{width:176px;height:131px;background:var(--navy);display:flex;align-items:center;justify-content:center}
.step-label{margin-top:22px;font-size:17px;line-height:22px;letter-spacing:1px;height:70px}
.step-label small{display:block;font-size:12px;line-height:14px;letter-spacing:0}
.btn-blue{display:block;margin:0 auto;width:156px;height:42px;line-height:42px;background:var(--btn-blue);color:var(--white);font-weight:700;font-size:18px;border-radius:6px}

/* mission */
.mission-title{left:0;top:1944px;width:1200px;font-size:34px;font-weight:700}
.mission-text{left:112px;top:2003px;width:976px;font-size:17px;line-height:30px;letter-spacing:.8px}
.mission-btn{left:511px;top:2128px;width:207px;height:42px;line-height:42px}

/* faq */
.faq{left:0;top:2248px;width:1200px;height:545px;background:var(--grey)}
.faq-title{left:0;top:2286px;width:1200px;font-size:35px;font-weight:700;letter-spacing:2px}
.faq-art{left:123px;top:2362px;width:443px;height:355px;border:10px solid #acd6ee;background:linear-gradient(135deg,#fdf3c9,#f6d68a)}
.faq-row{left:602px;width:478px;height:40px;background:var(--row);font-size:16px;line-height:40px;padding-left:24px;letter-spacing:.6px}
.faq-row svg{position:absolute;right:20px;top:14px}

/* footer */
.site-footer{left:0;top:2793px;width:1200px;height:304px;background:var(--footer)}
.footer-car{left:0;top:2945px;width:210px;height:135px;border-radius:60px 80px 20px 20px;background:linear-gradient(180deg,#45c6f2,#1c8fd0)}
.footer-head{top:2858px;color:var(--white);font-weight:700;font-size:18px;letter-spacing:.5px;padding-bottom:6px;border-bottom:2px solid var(--white)}
.footer-text{color:var(--white);font-size:15px;line-height:31px}
.news-input{left:851px;top:2994px;width:186px;height:32px;background:var(--white);font-size:11px;line-height:32px;padding-left:10px;color:#999}
.news-btn{left:1037px;top:2994px;width:38px;height:32px;background:var(--navy);display:flex;align-items:center;justify-content:center}
.bottom-bar{left:0;top:3097px;width:1200px;height:72px;background:var(--footer-dark)}
.legal{left:118px;top:3124px;color:var(--white);font-size:14px}
.social{top:3118px;width:32px;height:32px;border-radius:50%;background:var(--footer)}
</style>
</head>
<body>

<header class="site-header abs">
  <div class="brand abs"><span class="brand-dot"></span>Bikes for Dreams</div>
  <div class="phone abs">1-800-555-0199</div>
  <div class="btn-red header-donate abs">DONATE NOW</div>
  <nav class="main-nav abs">
    <a class="active">HOME</a><a>ABOUT</a><a>HOW TO DONATE</a><a>FAQ</a><a>BLOG</a>
  </nav>
</header>

<section class="hero abs"></section>
<div class="hero-art abs" role="img" aria-label="Illustrated city skyline with two cartoon cars"></div>
<div class="hero-title abs center">WE DO THE WORK. YOU ENJOY<br>THE TAX BENEFITS!</div>
<div class="btn-red hero-donate abs">DONATE NOW</div>
<svg class="slide-arrow abs" style="left:50px" width="36" height="40" viewBox="0 0 36 40"><path d="M30 2 L8 20 L30 38 L30 28 L20 20 L30 12Z" fill="#1e88c9"/></svg>
<svg class="slide-arrow abs" style="left:795px" width="36" height="40" viewBox="0 0 36 40"><path d="M6 2 L28 20 L6 38 L6 28 L16 20 L6 12Z" fill="#1e88c9"/></svg>
<div class="dots abs"><span></span><span></span><span></span><span></span></div>

<form class="donate-form abs">
  <div class="form-head">DONATING IS SIMPLE</div>
  <div class="form-field" style="top:76px">Car / Automobiles</div>
  <div class="form-field" style="top:123px">Name</div>
  <div class="form-field" style="top:170px">Phone</div>
  <div class="form-field" style="top:217px">Email</div>
  <div class="form-field" style="top:264px">Picup Address</div>
  <div class="form-field" style="top:311px">Pickup Address One*</div>
  <div class="form-field" style="top:358px">Pickup Address Two*</div>
  <div class="form-field" style="top:405px">Pickup City*</div>
  <div class="form-field" style="top:452px">Pickup Zip Code</div>
  <div class="form-field" style="top:499px">Pickup Estate*</div>
  <div class="form-field" style="top:546px;padding-left:30px">Pickup Zip Code</div>
</form>

<h2 class="intro-title abs center">DONATE CAR TO CHARITY</h2>
<p class="intro-sub abs center">Your car can make a difference</p>
<div class="btn-navy intro-btn abs">Read More</div>

<section class="features abs">
  <div class="feature abs" style="left:70px;top:50px">
    <div class="feature-circle"><svg width="80" height="50" viewBox="0 0 80 50" fill="#fff"><rect x="30" y="14" width="34" height="20"/><rect x="64" y="22" width="12" height="12"/><rect x="4" y="28" width="26" height="6"/><path d="M6 28 L24 4" stroke="#fff" stroke-width="3"/><circle cx="18" cy="40" r="6"/><circle cx="56" cy="40" r="6"/></svg></div>
    <div class="feature-label">Towing is Free</div>
  </div>
  <div class="feature abs" style="left:335px;top:50px">
    <div class="feature-circle"><svg width="76" height="76" viewBox="0 0 76 76" fill="none" stroke="#fff" stroke-width="4"><circle cx="38" cy="38" r="28"/><ellipse cx="38" cy="38" rx="12" ry="28"/><path d="M10 38h56M14 24h48M14 52h48"/></svg></div>
    <div class="feature-label">Donations Accepted<br>Nationwide</div>
  </div>
  <div class="feature abs" style="left:597px;top:50px">
    <div class="feature-circle"><svg width="76" height="76" viewBox="0 0 76 76" fill="none" stroke="#fff" stroke-width="6"><circle cx="38" cy="38" r="27"/><circle cx="38" cy="38" r="6" fill="#fff"/><path d="M12 34h52M38 44v20"/></svg></div>
    <div class="feature-label">All Vehicle Types<br>Welcome</div>
  </div>
  <div class="feature abs" style="left:861px;top:50px">
    <div class="feature-circle"><svg width="72" height="64" viewBox="0 0 72 64" fill="none" stroke="#fff" stroke-width="4"><path d="M6 28 L36 8 L66 28 V58 H6Z"/><rect x="18" y="4" width="36" height="30" fill="#fff" stroke="none"/><path d="M6 28 L36 46 L66 28"/></svg></div>
    <div class="feature-label">Tax Deductible</div>
  </div>
</section>

<section class="how abs"></section>
<h2 class="how-title abs center">HOW TO DONATE</h2>
<div class="kid abs" role="img" aria-label="Cartoon boy pointing toward the steps" style="left:0;top:1405px;width:186px;height:408px"></div>
<div class="kid abs" role="img" aria-label="Cartoon girl pointing toward the steps" style="left:1010px;top:1445px;width:190px;height:380px;background:linear-gradient(180deg,#f0b24a,#e8426a)"></div>
<div class="how-panel abs"></div>
<div class="step abs" style="left:192px;top:1517px">
  <div class="step-tile"><svg width="70" height="70" viewBox="0 0 70 70" fill="none" stroke="#fff" stroke-width="4"><circle cx="38" cy="34" r="24"/><text x="38" y="42" fill="#fff" stroke="none" font-family="Lato,sans-serif" font-weight="900" font-size="22" text-anchor="middle">24</text></svg></div>
  <div class="step-label">Fast Pickup<small>Same Day to 24<br>Hours.</small></div>
  <span class="btn-blue center">Read More</span>
</div>
<div class="step abs" style="left:395px;top:1517px">
  <div class="step-tile"><svg width="56" height="72" viewBox="0 0 56 72" fill="none" stroke="#fff" stroke-width="4"><rect x="4" y="8" width="48" height="60" rx="3"/><rect x="18" y="2" width="20" height="10" fill="#fff"/><path d="M14 28h28M14 38h28M14 48h20"/></svg></div>
  <div class="step-label">No Paperwork<br>Hassles</div>
  <span class="btn-blue center">Read More</span>
</div>
<div class="step abs" style="left:592px;top:1517px">
  <div class="step-tile"><svg width="70" height="70" viewBox="0 0 70 70" fill="none" stroke="#fff" stroke-width="4"><rect x="10" y="10" width="36" height="36" transform="rotate(-20 28 28)"/><circle cx="46" cy="56" r="7"/><circle cx="60" cy="46" r="7"/><path d="M30 30 L50 50M40 26 L56 40"/></svg></div>
  <div class="step-label">Income Tax<br>Deduction</div>
  <span class="btn-blue center">Read More</span>
</div>
<div class="step abs" style="left:792px;top:1517px">
  <div class="step-tile"><svg width="90" height="50" viewBox="0 0 90 50" fill="none" stroke="#fff" stroke-width="4"><path d="M4 40 C20 30 30 44 50 40 L70 34"/><path d="M40 24 L50 12 H70 L80 22 V30 H40Z" fill="#fff"/></svg></div>
  <div class="step-label">Car donations help<br>fund programs:</div>
  <span class="btn-blue center">Read More</span>
</div>

<h2 class="mission-title abs center">Our Mission</h2>
<p class="mission-text abs center">Lorem Ipsum is simply dummy text of the printing and typesetting industry. Lorem Ipsum has been the industry's<br>standard dummy text ever since the 1500s, when an unknown printer took a galley of type and scrambled<br>it to make a type specimen book.</p>
<div class="btn-navy mission-btn abs">Read More</div>

<section class="faq abs"></section>
<h2 class="faq-title abs center">FREQUENTLY ASKED QUESTIONS</h2>
<div class="faq-art abs" role="img" aria-label="Illustration of a friendly man in shirt and tie presenting the answers"></div>
<div class="faq-row abs" style="top:2373px">What types of vehicles can be donated?<svg width="16" height="12"><path d="M0 0H16L8 12Z" fill="#2d9ad8"/></svg></div>
<div class="faq-row abs" style="top:2434px">Lorem Ipsum is simply  text of the printing<svg width="16" height="12"><path d="M0 0H16L8 12Z" fill="#2d9ad8"/></svg></div>
<div class="faq-row abs" style="top:2493px">Lorem  simply dummy text of the?<svg width="16" height="12"><path d="M0 0H16L8 12Z" fill="#2d9ad8"/></svg></div>
<div class="faq-row abs" style="top:2554px">Lorem Ipsum the printing and industry<svg width="16" height="12"><path d="M0 0H16L8 12Z" fill="#2d9ad8"/></svg></div>
<div class="faq-row abs" style="top:2613px">Lorem Ipsum is simply industry. Lorem ?<svg width="16" height="12"><path d="M0 0H16L8 12Z" fill="#2d9ad8"/></svg></div>
<div class="faq-row abs" style="top:2675px">Lorem  and typesetting industry ?<svg width="16" height="12"><path d="M0 0H16L8 12Z" fill="#2d9ad8"/></svg></div>

<footer class="site-footer abs"></footer>
<div class="footer-car abs" role="img" aria-label="Cartoon light blue car"></div>
<div class="footer-head abs" style="left:118px">ABOUT US</div>
<p class="footer-text abs center" style="left:110px;top:2904px;width:330px">Lorem Ipsum is simply dummy text of the<br>Lorem typesetting industry. Lorem<br>been the industry's standard<br>dummy text ever since  1500.</p>
<div class="footer-head abs" style="left:526px">CONTACT US</div>
<p class="footer-text abs" style="left:526px;top:2911px">480 Maple Grove Avenue, Suite 210</p>
<p class="footer-text abs" style="left:526px;top:2962px;line-height:22px">Office Phone: 555 013 4477<br>Fax: 555 013 4478<br>hello@bikesfordreams.org</p>
<div class="footer-head abs" style="left:851px">NEWSLETTER SUBSCRIBE</div>
<p class="footer-text abs" style="left:851px;top:2912px;width:230px;font-size:13px;line-height:18px">We will inform you about newest project and promotions.Subscribe to our newsletter.</p>
<div class="news-input abs">Your Email Address</div>
<div class="news-btn abs"><svg width="16" height="12" viewBox="0 0 16 12" fill="none" stroke="#fff" stroke-width="2"><rect x="1" y="1" width="14" height="10"/><path d="M1 1L8 7L15 1"/></svg></div>

<div class="bottom-bar abs"></div>
<div class="legal abs">Privacy policy - Legal mentions - Terms and Conditions</div>
<span class="social abs" style="left:854px"></span>
<span class="social abs" style="left:903px"></span>
<span class="social abs" style="left:950px"></span>
<span class="social abs" style="left:998px"></span>
<span class="social abs" style="left:1045px"></span>

</body>
</html>
```